Songs Cover Art. Song tittle DJ K - Keep The Floor Lit

Hey

I need a cover art for my songs. My genre is Big Room House/EDM music and my DJ name is DJ K. Song title is Keep The Floor Lit. I'm a producer and i need a designer to design all my cover art so that i will be able upload my song with a cover art. Do let me know if you have any questions.

Song Tittle: Keep The Floor Lit
Artist name: DJ K

Thanks

Industry/Entity Type

House

Requirements
Should not have
• Please dont make the design to colourful.

```html
<!DOCTYPE html>
<html lang="en">
<head>
<meta charset="utf-8">
<title>DJ K – Keep The Floor Lit · Cover Art</title>
<link rel="stylesheet" href="https://fonts.googleapis.com/css2?family=Audiowide&display=swap">
<style>
  :root {
    --night: #140b12;
    --night-deep: #0c070b;
    --violet: #7a2fd6;
    --magenta: #d23be8;
    --indigo: #3a2aa8;
    --ink-white: #ffffff;
  }
  html, body {
    margin: 0;
    padding: 0;
    width: 1200px;
    height: 1200px;
    overflow: hidden;
    background: var(--night);
  }
  .cover {
    position: relative;
    width: 1200px;
    height: 1200px;
    overflow: hidden;
    background: radial-gradient(circle at 50% 50%, #1c0f1a 0%, var(--night) 55%, var(--night-deep) 100%);
  }
  .cover-art {
    position: absolute;
    inset: 0;
    width: 1200px;
    height: 1200px;
  }
  .title-block {
    position: absolute;
    inset: 0;
    width: 1200px;
    height: 1200px;
  }
  .title-line,
  .artist-name {
    font-family: "Audiowide", sans-serif;
    fill: var(--ink-white);
    text-transform: uppercase;
  }
  .title-line { font-size: 170px; }
  .artist-name { font-size: 80px; }
</style>
</head>
<body>
<main class="cover">
  <svg class="cover-art" viewBox="0 0 1200 1200" role="img"
       aria-label="Abstract illustration of a glowing purple and magenta sound-wave ring with a jagged neon waveform streaking horizontally across a dark background">
    <defs>
      <radialGradient id="ring-glow" cx="50%" cy="50%" r="50%">
        <stop offset="0%" stop-color="#2a1a5a" stop-opacity="0.9"/>
        <stop offset="55%" stop-color="#4a2a9a" stop-opacity="0.75"/>
        <stop offset="80%" stop-color="#b23ad8" stop-opacity="0.55"/>
        <stop offset="100%" stop-color="#140b12" stop-opacity="0"/>
      </radialGradient>
      <linearGradient id="wave-band" x1="0" y1="0" x2="1" y2="0">
        <stop offset="0%" stop-color="#d23be8" stop-opacity="0"/>
        <stop offset="20%" stop-color="#7a2fd6" stop-opacity="0.55"/>
        <stop offset="50%" stop-color="#3a2aa8" stop-opacity="0.7"/>
        <stop offset="80%" stop-color="#7a2fd6" stop-opacity="0.55"/>
        <stop offset="100%" stop-color="#d23be8" stop-opacity="0"/>
      </linearGradient>
    </defs>
    <circle cx="640" cy="590" r="420" fill="url(#ring-glow)"/>
    <ellipse cx="600" cy="560" rx="620" ry="110" fill="url(#wave-band)"/>
  </svg>

  <svg class="title-block" viewBox="0 0 1200 1200">
    <text class="title-line" x="135" y="592" textLength="1005" lengthAdjust="spacingAndGlyphs">Keep The</text>
    <text class="title-line" x="95" y="810" textLength="1010" lengthAdjust="spacingAndGlyphs">Floor Lit</text>
    <text class="artist-name" x="492" y="950" textLength="220" lengthAdjust="spacingAndGlyphs">DJ K</text>
  </svg>
</main>
</body>
</html>
```